VR Business Card

Design new business cards for VELMOsoft

Please see attached for the design brief

**** Please note, please feel free to propose a font that works for a professional, technology company ***

Target Market(s)

Technology buyers

Industry/Entity Type

Business

```html
<!DOCTYPE html>
<html lang="en">
<head>
<meta charset="utf-8">
<title>VELMOsoft Business Card</title>
<link rel="stylesheet" href="https://fonts.googleapis.com/css2?family=Source+Sans+3:wght@400;600&display=swap">
<style>
  :root {
    --page-bg: #e4e4e2;
    --card-black: #141414;
    --card-black-light: #2a2a2a;
    --accent-blue: #1a93cf;
    --text-white: #ffffff;
    --text-soft: #c9c9c9;
    --sans: "Source Sans 3", "Myriad Pro", sans-serif;
  }
  * { box-sizing: border-box; margin: 0; padding: 0; }
  html, body { width: 1200px; height: 1000px; overflow: hidden; }
  body {
    background: var(--page-bg);
    font-family: var(--sans);
    position: relative;
  }
  .card {
    position: absolute;
    left: 280px;
    width: 640px;
    height: 366px;
    background: linear-gradient(160deg, var(--card-black-light) 0%, var(--card-black) 55%, #0c0c0c 100%);
    box-shadow: 0 10px 28px rgba(0,0,0,0.25);
    overflow: hidden;
    color: var(--text-white);
  }
  .card--back { top: 80px; }
  .card--front { top: 520px; }

  /* Back side */
  .back__bar-top {
    position: absolute; right: 0; top: 40px;
    width: 110px; height: 36px; background: var(--accent-blue);
  }
  .back__bar-bottom {
    position: absolute; left: 0; top: 220px;
    width: 120px; height: 36px; background: var(--accent-blue);
  }
  .brand {
    position: absolute; left: 190px; top: 144px;
    font-size: 30px; font-weight: 400; color: var(--text-white);
    text-transform: uppercase; letter-spacing: 2px;
  }
  .tagline {
    position: absolute; left: 420px; top: 154px;
    font-size: 14px; font-weight: 400; color: var(--text-soft);
  }
  .back__address, .back__web {
    position: absolute; top: 270px;
    display: flex; align-items: flex-start; gap: 8px;
    font-size: 11px; line-height: 1.35; color: var(--text-soft);
  }
  .back__address { left: 200px; }
  .back__web { left: 410px; align-items: center; }
  .icon { width: 16px; height: 16px; flex: none; }

  /* Front side */
  .front__band {
    position: absolute; left: 0; right: 0; top: 150px;
    height: 60px; background: var(--accent-blue);
  }
  .front__name {
    position: absolute; left: 0; right: 0; top: 100px;
    text-align: center; line-height: 44px;
    font-size: 36px; font-weight: 600; letter-spacing: 0.5px;
  }
  .front__title {
    position: absolute; left: 0; right: 0; top: 150px;
    text-align: center; line-height: 60px;
    font-size: 24px; font-weight: 400;
  }
  .contact {
    position: absolute; left: 120px; top: 232px; width: 400px;
    font-size: 17px; color: var(--text-white);
  }
  .contact__row {
    display: flex; justify-content: center; gap: 26px; margin-bottom: 6px;
  }
  .contact__item { display: flex; align-items: center; gap: 7px; }
</style>
</head>
<body>

<section class="card card--back" aria-label="Business card back">
  <div class="back__bar-top"></div>
  <div class="back__bar-bottom"></div>
  <p class="brand">VELMOsoft</p>
  <p class="tagline">Software built to last</p>
  <div class="back__address">
    <svg class="icon" viewBox="0 0 16 16" fill="none" stroke="#1a93cf" stroke-width="1.4">
      <path d="M8 15s5-5 5-8.5A5 5 0 0 0 3 6.5C3 10 8 15 8 15z"/><circle cx="8" cy="6.5" r="1.8"/>
    </svg>
    <p>VELMOsoft Solutions<br>Lindenweg 8, 4410 Liestal<br>Switzerland</p>
  </div>
  <div class="back__web">
    <svg class="icon" viewBox="0 0 16 16" fill="none" stroke="#1a93cf" stroke-width="1.3">
      <circle cx="8" cy="8" r="6.5"/><ellipse cx="8" cy="8" rx="3" ry="6.5"/><path d="M1.5 8h13"/>
    </svg>
    <p>http://velmosoft.example</p>
  </div>
</section>

<section class="card card--front" aria-label="Business card front">
  <div class="front__band"></div>
  <h1 class="front__name">MARTIN HALE</h1>
  <p class="front__title">CEO</p>
  <div class="contact">
    <div class="contact__row">
      <span class="contact__item">
        <svg class="icon" viewBox="0 0 16 16" fill="none" stroke="#1a93cf" stroke-width="1.3"><circle cx="8" cy="8" r="7"/><path d="M5.5 4.5l1.5 2-1 1c.6 1.2 1.4 2 2.5 2.5l1-1 2 1.5-1 1.5C7.5 12 4 8.5 4 5.5z"/></svg>
        +41 44 620 1180
      </span>
    </div>
    <div class="contact__row">
      <span class="contact__item">
        <svg class="icon" viewBox="0 0 16 16" fill="none" stroke="#1a93cf" stroke-width="1.3"><circle cx="8" cy="8" r="7"/><path d="M5.5 4.5l1.5 2-1 1c.6 1.2 1.4 2 2.5 2.5l1-1 2 1.5-1 1.5C7.5 12 4 8.5 4 5.5z"/></svg>
        +41 44 620 1181
      </span>
      <span class="contact__item">
        <svg class="icon" viewBox="0 0 16 16" fill="none" stroke="#1a93cf" stroke-width="1.3"><rect x="4.5" y="1.5" width="7" height="13" rx="1.2"/><path d="M7 12.5h2"/></svg>
        +41 79 305 4417
      </span>
    </div>
    <div class="contact__row">
      <span class="contact__item">
        <svg class="icon" viewBox="0 0 16 16" fill="none" stroke="#1a93cf" stroke-width="1.3"><rect x="2" y="6" width="12" height="7" rx="1"/><rect x="4.5" y="2.5" width="7" height="3.5"/><path d="M5 9.5h6"/></svg>
        +41 800 004 210
      </span>
    </div>
    <div class="contact__row">
      <span class="contact__item">
        <svg class="icon" viewBox="0 0 16 16" fill="none" stroke="#1a93cf" stroke-width="1.3"><rect x="1.5" y="3.5" width="13" height="9"/><path d="M1.5 3.5L8 9l6.5-5.5"/></svg>
        martin.hale@velmosoft.example
      </span>
    </div>
  </div>
</section>

</body>
</html>
```